Business Card Design

We need a business card design for a consulting firm which provides safety and risk management consulting services for public venues, hotels and tourist attractions. The business card design should include the attached logo unedited with a design based on incorporating the existing logo with a design of geometric patterns or lines on a predominantly white background.

Industry/Entity Type

Business

Contact Information for Business Card

Dane Morvello
Director & Principal Consultant

Ph: +61 (0) 468502 174
PO Box 456 Kellmore Vale, NSW Australia 2563
info@corvanwellandcare.com

(back of card to include website www.corvanwellandcare.com

```html
<!DOCTYPE html>
<html lang="en">
<head>
<meta charset="utf-8">
<title>Corvan Welland Care – Business Card</title>
<link rel="stylesheet" href="https://fonts.googleapis.com/css2?family=Open+Sans:wght@400;600;700;800&display=swap">
<style>
  :root{
    --bg:#e9ecef;
    --card-white:#ffffff;
    --brand-blue:#1a9ad6;
    --brand-blue-light:#35b3e6;
    --brand-green:#6cb33f;
    --ink:#2f4f6b;
    --muted:#7f8c96;
    --white:#ffffff;
  }
  *{box-sizing:border-box;margin:0;padding:0}
  html,body{width:1200px;height:948px;overflow:hidden}
  body{
    background:var(--bg);
    font-family:"Open Sans",Arial,sans-serif;
    display:flex;flex-direction:column;align-items:center;justify-content:center;gap:50px;
  }
  .card{
    width:740px;height:423px;position:relative;overflow:hidden;
    box-shadow:0 6px 22px rgba(0,0,0,.14);
  }
  /* Front */
  .card--front{background:var(--card-white)}
  .brand{
    position:absolute;left:250px;top:62px;
    display:flex;align-items:center;gap:14px;
  }
  .brand__dot{width:34px;height:34px;border-radius:50%;background:var(--brand-green)}
  .brand__name{
    font-weight:800;font-size:34px;letter-spacing:.5px;color:var(--brand-blue);
    text-transform:uppercase;line-height:1;
  }
  .tagline{
    position:absolute;left:298px;top:108px;
    font-size:9px;font-weight:600;letter-spacing:1.4px;color:var(--muted);text-transform:uppercase;
  }
  .person{position:absolute;left:298px;top:152px}
  .person__name{font-size:22px;font-weight:700;color:var(--ink)}
  .person__role{font-size:15px;font-weight:400;color:var(--brand-green);margin-top:2px}
  .contact-band{
    position:absolute;left:0;right:0;bottom:0;height:150px;
    background:var(--brand-blue);
    padding:22px 0 0 60px;
    display:flex;flex-direction:column;gap:12px;
  }
  .contact{display:flex;align-items:center;gap:14px;color:var(--white);font-size:15px}
  .contact__icon{
    width:26px;height:26px;border-radius:50%;background:var(--white);
    display:flex;align-items:center;justify-content:center;flex:none;
  }
  .contact__icon svg{width:14px;height:14px;fill:var(--brand-blue)}
  /* Back */
  .card--back{
    background:linear-gradient(160deg,var(--brand-blue-light),var(--brand-blue));
    display:flex;flex-direction:column;align-items:center;justify-content:center;gap:26px;
  }
  .back-brand{display:flex;align-items:center;gap:16px}
  .back-brand__circle{width:60px;height:60px;border-radius:50%;border:4px solid var(--white)}
  .back-brand__name{font-weight:800;font-size:36px;color:var(--white);text-transform:uppercase;line-height:1}
  .website{color:var(--white);font-size:15px;letter-spacing:1px}
</style>
</head>
<body>
  <section class="card card--front" aria-label="Business card front">
    <div class="brand">
      <span class="brand__dot"></span>
      <span class="brand__name">Corvan Welland Care</span>
    </div>
    <p class="tagline">Keeping people and places safe every day</p>
    <div class="person">
      <p class="person__name">Dane Morvello</p>
      <p class="person__role">Director &amp; Principal Consultant</p>
    </div>
    <div class="contact-band">
      <p class="contact">
        <span class="contact__icon"><svg viewBox="0 0 24 24"><path d="M6.6 10.8a15.1 15.1 0 0 0 6.6 6.6l2.2-2.2c.3-.3.7-.4 1-.2 1.1.4 2.3.6 3.6.6.6 0 1 .4 1 1V20c0 .6-.4 1-1 1A17 17 0 0 1 3 4c0-.6.4-1 1-1h3.5c.6 0 1 .4 1 1 0 1.3.2 2.5.6 3.6.1.3 0 .7-.2 1z"/></svg></span>
        +61 (0) 468502 174
      </p>
      <p class="contact">
        <span class="contact__icon"><svg viewBox="0 0 24 24"><path d="M12 2a7 7 0 0 0-7 7c0 5.2 7 13 7 13s7-7.8 7-13a7 7 0 0 0-7-7zm0 9.5A2.5 2.5 0 1 1 12 6.5a2.5 2.5 0 0 1 0 5z"/></svg></span>
        PO Box 456 Kellmore Vale, NSW Australia 2563
      </p>
      <p class="contact">
        <span class="contact__icon"><svg viewBox="0 0 24 24"><path d="M3 5h18v14H3zm2 2v.5l7 4.5 7-4.5V7zm0 2.8V17h14V9.8l-7 4.5z"/></svg></span>
        info@corvanwellandcare.com
      </p>
    </div>
  </section>

  <section class="card card--back" aria-label="Business card back">
    <div class="back-brand">
      <span class="back-brand__circle"></span>
      <span class="back-brand__name">Corvan Welland Care</span>
    </div>
    <p class="website">www.corvanwellandcare.com</p>
  </section>
</body>
</html>
```